ZMobvra - Tenant Place Services

Want Quality Tenants?!

Tenant Placement is a service that allows landlords to leave the stress of filling vacancies behind.
zMobvra provides landlords, investors and property manager's a system to occupy vacancies with qualified tenants Faster, Cheaper, Easier
zMobvra takes the hassle out of the rental process from searching for tenants to move-in inspections.

Reason: I'm extending the deadline because I want to give other designers an opportunity to submit and I have a couple designs that I'm awaiting current designers to resubmit some designs.

```html
<!DOCTYPE html>
<html lang="en">
<head>
<meta charset="utf-8">
<title>zMobvra – Tenant Placement</title>
<link rel="stylesheet" href="https://fonts.googleapis.com/css2?family=Oswald:wght@500;600;700&family=Open+Sans:wght@400&display=swap">
<style>
  :root {
    --green-light: #6cc22c;
    --green-dark: #2f8a16;
    --edge-brown: #8a5a32;
    --white: #ffffff;
    --orange-top: #ffd23a;
    --orange-bottom: #f07a12;
    --button-top: #f7932e;
    --button-bottom: #d9560c;
    --button-arrow: #e96c1a;
    --brand-green: #5aa832;
    --photo-warm: #c9b59a;
    --photo-cool: #8c7a68;
  }
  html, body {
    margin: 0;
    padding: 0;
    width: 1200px;
    height: 840px;
    overflow: hidden;
    background: var(--white);
  }
  .ad {
    position: relative;
    width: 1200px;
    height: 840px;
    overflow: hidden;
    font-family: "Oswald", "Arial Narrow", sans-serif;
  }
  .ad__shapes {
    position: absolute;
    inset: 0;
  }
  .headline {
    position: absolute;
    left: 42px;
    top: 78px;
    margin: 0;
    font-size: 72px;
    font-weight: 700;
    line-height: 1;
    letter-spacing: 0.5px;
    background: linear-gradient(180deg, var(--orange-top) 0%, var(--orange-bottom) 100%);
    -webkit-background-clip: text;
    background-clip: text;
    color: transparent;
    text-shadow: none;
    filter: drop-shadow(2px 3px 2px rgba(0,0,0,0.35));
  }
  .divider {
    position: absolute;
    left: 60px;
    top: 232px;
    width: 440px;
    height: 2px;
    background: linear-gradient(90deg, rgba(255,255,255,0) 0%, rgba(255,255,255,0.55) 50%, rgba(255,255,255,0) 100%);
  }
  .tagline {
    position: absolute;
    left: 30px;
    top: 282px;
    width: 560px;
    margin: 0;
    text-align: center;
    color: var(--white);
    font-size: 74px;
    font-weight: 500;
    line-height: 89px;
    text-shadow: 2px 3px 3px rgba(0,0,0,0.3);
  }
  .cta {
    position: absolute;
    left: 91px;
    top: 694px;
    width: 334px;
    height: 98px;
    display: flex;
    border-radius: 8px;
    overflow: hidden;
    box-shadow: 0 4px 8px rgba(0,0,0,0.35);
    background: linear-gradient(180deg, var(--button-top), var(--button-bottom));
    text-decoration: none;
  }
  .cta__label {
    flex: 1;
    display: flex;
    align-items: center;
    justify-content: center;
    color: var(--white);
    font-size: 44px;
    font-weight: 600;
    text-shadow: 1px 2px 2px rgba(0,0,0,0.3);
  }
  .cta__arrow {
    width: 74px;
    display: flex;
    align-items: center;
    justify-content: center;
    border-left: 2px solid rgba(255,255,255,0.35);
    background: var(--button-arrow);
  }
  .brand {
    position: absolute;
    left: 700px;
    top: 745px;
    width: 360px;
    text-align: center;
    font-family: "Open Sans", Arial, sans-serif;
    font-weight: 400;
    font-size: 40px;
    color: var(--brand-green);
  }
</style>
</head>
<body>
<div class="ad">
  <svg class="ad__shapes" width="1200" height="840" viewBox="0 0 1200 840">
    <defs>
      <linearGradient id="panelGreen" x1="0" y1="0" x2="0" y2="1">
        <stop offset="0" stop-color="var(--green-light)"/>
        <stop offset="1" stop-color="var(--green-dark)"/>
      </linearGradient>
      <linearGradient id="photoTone" x1="0" y1="0" x2="1" y2="1">
        <stop offset="0" stop-color="var(--photo-warm)"/>
        <stop offset="1" stop-color="var(--photo-cool)"/>
      </linearGradient>
    </defs>
    <rect class="photo-area" x="540" y="0" width="660" height="602" fill="url(#photoTone)" role="img" aria-label="Photo of a smiling couple sitting on the floor among moving boxes, holding up new house keys"/>
    <path class="panel-edge" d="M0 0 H660 Q600 420 588 840 H0 Z" fill="var(--edge-brown)"/>
    <path class="panel" d="M0 0 H638 Q578 420 566 840 H0 Z" fill="url(#panelGreen)"/>
  </svg>

  <h1 class="headline">NEED TENANTS?!</h1>
  <div class="divider"></div>
  <p class="tagline">Fill your vacancy<br>Faster, Easier,<br>Cheaper</p>

  <a class="cta" href="#">
    <span class="cta__label">LEARN MORE</span>
    <span class="cta__arrow">
      <svg width="30" height="38" viewBox="0 0 30 38"><path d="M6 4 L24 19 L6 34" fill="none" stroke="#ffffff" stroke-width="7" stroke-linejoin="round"/></svg>
    </span>
  </a>

  <div class="brand">zMobvra</div>
</div>
</body>
</html>
```